New shirt company looking for a fun and edgy online retail website design

We're a new company looking for a simple yet attractive website to sell shirts/tops to a mostly younger female audience. Our name is Tavi Shirt Co. and the PlanHerd logo is uploaded. We're thinking a home page, three separate pages for our shirt "collections", and a contact page/cart page for a grand total of 5 pages. We'd like the website to be coded, easy for the consumer to navigate/shop/checkout, and easy to link to various social media platforms and online websites. For colors, we're aiming for various blues, light grey, and maybe tan/khaki. Our goal is to launch with approximately 20-30 tops/shirts (or 7-10) per page. Please let us know if you have any questions and thank you for helping us! We are very excited to see what is created!

Target Market(s)

Female teens to early twenties

Coding

Coded - Design and coding required

Number of Pages Required

3 page

Font styles to use
Decorative
Script

Colors
cee9f5
85cae6
33a6d7
0393ce
cfdfed
85acd3

Requirements
Must have
• Online shopping/purchasing capabilities, dropdowns to select sizes for each item, easy to add/remove new or seasoned items.

```html
<!DOCTYPE html>
<html lang="en">
<head>
<meta charset="utf-8">
<title>Tavi Shirt Co. — Home</title>
<link href="https://fonts.googleapis.com/css2?family=Lato:wght@300;400;700;900&display=swap" rel="stylesheet">
<style>
:root{
  --navy:#0b3f94;
  --sky:#88ceeb;
  --sky-text:#6cc2e8;
  --grey-bg:#f4f4f4;
  --circle:#efefef;
  --text-grey:#8a8a8a;
  --text-dark:#6b6b6b;
  --white:#ffffff;
  --star:#f5c518;
}
*{margin:0;padding:0;box-sizing:border-box}
html,body{width:1200px;height:3548px;overflow:hidden;background:var(--white)}
body{font-family:'Lato',sans-serif;position:relative;color:var(--text-dark)}
.abs{position:absolute}
a{color:inherit;text-decoration:none}

/* header */
.site-header{left:0;top:0;width:1200px;height:65px;background:var(--sky)}
.brand{left:150px;top:10px;width:114px;height:45px;border:2px solid var(--navy);display:flex;align-items:center;justify-content:center;color:var(--navy);font-weight:700;font-size:13px;letter-spacing:.5px}
.main-nav{left:559px;top:0;height:65px;display:flex}
.main-nav a{height:65px;line-height:73px;padding:0 13px;font-size:11.5px;color:var(--white);text-transform:uppercase}
.main-nav a.active{background:var(--navy);padding:0 11px}
.header-icons{left:972px;top:26px;display:flex;gap:14px;align-items:center}
.cart-badge{position:absolute;left:60px;top:10px;width:13px;height:13px;border-radius:50%;background:var(--navy);color:#fff;font-size:8px;text-align:center;line-height:13px;font-weight:700}

/* hero */
.hero-circle{left:572px;width:548px;height:548px;border-radius:50%;background:var(--circle)}
.hero-clip{left:0;top:65px;width:1200px;height:606px;overflow:hidden}
.hero-photo{left:661px;top:38px;width:428px;height:568px;background:linear-gradient(180deg,#c9a37a 0%,#8c8c8c 45%,#707070 70%,#4c6a92 100%);border-radius:200px 200px 0 0}
.hero-kicker{left:151px;top:272px;font-size:31px;color:var(--sky-text);font-weight:400;letter-spacing:.5px}
.hero-title{left:149px;top:300px;font-size:71px;color:var(--navy);font-weight:900;letter-spacing:1px;line-height:1}
.hero-sub{left:287px;top:368px;font-size:36px;color:var(--sky-text);font-weight:400}
.hero-text{left:150px;top:417px;font-size:11px;color:var(--text-grey)}
.btn-outline{display:block;border:2px solid var(--navy);color:var(--navy);font-size:11px;text-align:center;text-transform:uppercase;background:transparent}
.hero-btn{left:150px;top:467px;width:122px;height:41px;line-height:37px}
.dots{display:flex;gap:9px}
.dots span{width:8px;height:8px;border:1px solid var(--navy)}
.dots span.on{background:var(--navy)}
.hero-dots{left:157px;top:600px}

/* categories */
.category{top:685px;height:258px;background:var(--grey-bg);overflow:hidden}
.category .ph{position:absolute;top:0;height:258px}
.category h3{position:absolute;font-size:30px;color:var(--navy);font-weight:700;top:93px}
.category p{position:absolute;font-size:10.5px;color:var(--text-grey);width:135px;line-height:13px;top:136px}

/* section titles */
.section-title{left:0;width:1200px;text-align:center;font-size:27px;color:var(--navy);font-weight:700}

/* products */
.arrow-box{width:42px;height:42px;border:1px solid #c9c9c9;display:flex;align-items:center;justify-content:center;background:#fff}
.product .ph{width:212px;height:296px}
.product .name{margin-top:23px;margin-left:5px;font-size:18px;color:var(--text-dark);font-weight:400}
.product .price{margin-left:5px;margin-top:2px;font-size:12.5px;color:var(--navy);font-weight:700}
.add-bar{position:absolute;left:0;top:253px;width:212px;height:43px;background:var(--navy);color:#fff;font-size:11.5px;text-align:center;line-height:43px;text-transform:uppercase}
.shade{position:absolute;left:0;top:0;width:212px;height:296px;background:rgba(0,0,0,.45)}

/* sale */
.sale-band{left:0;top:1548px;width:594px;height:472px;background:var(--sky)}
.sale-frame{left:26px;top:1569px;width:540px;height:429px;border:10px solid #fff;background:var(--sky)}
.sale-photo-frame{left:514px;top:1592px;width:686px;height:384px;background:#fff}
.sale-photo{left:521px;top:1599px;width:679px;height:371px;background:linear-gradient(90deg,#f3efec 0%,#e7d6cc 45%,#7a5a4e 60%,#efe8e3 100%)}
.sale-title{left:149px;top:1655px;font-size:58px;color:#fff;font-weight:700;letter-spacing:.5px}
.sale-sub{left:149px;top:1727px;font-size:25px;color:#fff;font-weight:700}
.sale-text{left:149px;top:1770px;width:340px;font-size:10.5px;color:#fff;line-height:22.5px}
.sale-btn{left:150px;top:1860px;width:122px;height:40px;line-height:36px}

/* news */
.news-card{top:2198px;width:287px}
.news-card .ph{width:287px;height:180px}
.news-card .head{margin-top:20px;margin-left:1px;font-size:13px;color:var(--sky-text);text-transform:uppercase}
.news-card .date{margin-top:4px;margin-left:1px;font-size:11.5px;color:var(--navy)}
.news-card .text{margin-top:9px;margin-left:3px;font-size:10.5px;color:var(--text-grey);line-height:18px;width:285px}
.news-card .more{display:inline-block;margin-top:29px;margin-left:3px;font-size:11px;color:var(--navy);text-decoration:underline}

/* testimonials */
.quote{left:232px;top:2733px;width:710px;text-align:center;font-size:10.5px;color:var(--text-grey);line-height:22px}
.qmark{font-size:26px;color:#aaa;font-family:Georgia,serif;vertical-align:-9px;font-weight:700;letter-spacing:-2px}
.t-name{left:0;top:2796px;width:1200px;text-align:center;font-size:13px;color:var(--navy)}
.t-stars{left:0;top:2820px;width:1200px;text-align:center;font-size:11px;color:var(--star);letter-spacing:1px}
.t-dots{left:571px;top:2880px}

/* service boxes */
.service{top:2989px;height:112px;display:flex;align-items:center;color:#fff}
.service.dark{background:var(--navy)}
.service.light{background:var(--sky)}
.service svg{margin-left:40px;flex:none}
.service .body{margin-left:28px}
.service h4{font-size:13px;font-weight:700;text-transform:uppercase;margin-bottom:6px}
.service p{font-size:10.5px;line-height:13px;width:160px}

/* footer */
.site-footer{left:0;top:3178px;width:1200px;height:314px;background:var(--sky)}
.footer-brand{left:150px;top:3230px;width:134px;height:54px;border:2px solid var(--navy);display:flex;align-items:center;justify-content:center;color:var(--navy);font-weight:700;font-size:15px}
.contact-list{left:153px;top:3319px;list-style:none;font-size:11px;color:#fff;line-height:18px}
.contact-list li{display:flex;align-items:center;gap:8px}
.contact-list li.indent{padding-left:22px}
.pay-row{left:150px;top:3421px;display:flex;gap:5px}
.pay-row span{width:31px;height:18px;background:#fff;border:1px solid #d9d9d9}
.footer-col h5{font-size:13px;color:var(--navy);font-weight:700;text-transform:uppercase;margin-bottom:42px}
.footer-col ul{list-style:none;font-size:11px;color:#fff;line-height:18px}
.news-input{left:743px;top:3317px;width:307px;height:39px;border:2px solid #fff;color:#fff;font-size:11px;padding-left:18px;line-height:35px}
.news-btn{left:743px;top:3365px;width:122px;height:40px;border:2px solid var(--navy);color:var(--navy);font-size:11px;text-align:center;line-height:36px;text-transform:uppercase}
.social-row{left:743px;top:3418px;display:flex;gap:11px}
.social-row span{width:19px;height:19px;border:2px solid var(--navy)}
.social-row span.fill{background:var(--navy)}
.bottom-bar{left:0;top:3492px;width:1200px;height:56px;background:var(--navy);color:#fff;font-size:11.5px}
.bottom-bar .copy{position:absolute;left:150px;top:21px}
.bottom-bar .legal{position:absolute;right:150px;top:21px}
</style>
</head>
<body>

<header class="abs site-header">
  <div class="abs brand">Tavi Shirt Co.</div>
  <nav class="abs main-nav">
    <a class="active" href="#">Home</a><a href="#">Collection</a><a href="#">About</a><a href="#">News</a><a href="#">Sale</a><a href="#">Contact</a>
  </nav>
  <div class="abs header-icons">
    <svg width="14" height="14" viewBox="0 0 14 14" fill="none" stroke="#fff" stroke-width="1.4"><circle cx="6" cy="6" r="4.5"/><path d="M9.5 9.5L13 13"/></svg>
    <svg width="14" height="14" viewBox="0 0 14 14" fill="none" stroke="#fff" stroke-width="1.3"><circle cx="7" cy="4.5" r="3"/><path d="M1.5 13.5c0-3 2.5-5 5.5-5s5.5 2 5.5 5"/></svg>
    <svg width="14" height="15" viewBox="0 0 14 15" fill="none" stroke="#fff" stroke-width="1.3"><rect x="1.5" y="4.5" width="11" height="9.5"/><path d="M4.5 4.5V3a2.5 2.5 0 015 0v1.5"/></svg>
    <span class="cart-badge">3</span>
  </div>
</header>

<section class="abs hero-clip">
  <div class="abs hero-circle" style="top:174px"></div>
  <div class="abs hero-photo" role="img" aria-label="Smiling young woman in sunglasses wearing a grey graphic tee and jeans"></div>
</section>
<div class="abs hero-kicker">THE MOST</div>
<div class="abs hero-title">TRENDY</div>
<div class="abs hero-sub">FASHION</div>
<p class="abs hero-text">Lorem Ipsum is simply dummy text of the printing and typesetting industry.</p>
<a class="abs btn-outline hero-btn" href="#">Shop now</a>
<div class="abs dots hero-dots"><span class="on"></span><span></span><span></span><span></span></div>

<div class="abs category" style="left:0;width:373px">
  <div class="ph" role="img" aria-label="Woman in a white ruffled off-shoulder crop top" style="left:48px;width:172px;background:linear-gradient(180deg,#d9c3b3 0%,#f7f7f7 50%,#e9e9e9 100%)"></div>
  <h3 style="left:222px">TOPS</h3>
  <p style="left:228px">Lorem Ipsum is simply dummy text of the printing and typesetting industry.</p>
</div>
<div class="abs category" style="left:389px;width:398px">
  <h3 style="left:38px">T-SHIRT</h3>
  <p style="left:43px">Lorem Ipsum is simply dummy text of the printing and typesetting industry.</p>
  <div class="ph" role="img" aria-label="Woman in a black printed t-shirt" style="left:197px;width:158px;background:linear-gradient(180deg,#e4cdb5 0%,#2a2a2a 35%,#1c1c1c 100%)"></div>
</div>
<div class="abs category" style="left:802px;width:398px">
  <h3 style="left:30px">SHIRT</h3>
  <p style="left:30px">Lorem Ipsum is simply dummy text of the printing and typesetting industry.</p>
  <div class="ph" role="img" aria-label="Woman in a red plaid button shirt" style="left:156px;width:206px;background:linear-gradient(180deg,#3a2a25 0%,#e0bfae 30%,#c4303a 60%,#9a2b35 100%)"></div>
</div>

<h2 class="abs section-title" style="top:1000px">FEATURE PRODUCTS</h2>
<div class="abs arrow-box" style="left:52px;top:1213px"><svg width="10" height="16" viewBox="0 0 10 16" fill="none" stroke="#999" stroke-width="1.2"><path d="M8 1L2 8l6 7"/></svg></div>
<div class="abs arrow-box" style="left:1108px;top:1213px"><svg width="10" height="16" viewBox="0 0 10 16" fill="none" stroke="#999" stroke-width="1.2"><path d="M2 1l6 7-6 7"/></svg></div>

<div class="abs product" style="left:149px;top:1086px">
  <div class="ph" role="img" aria-label="Model in an oversized white graphic tee" style="background:linear-gradient(180deg,#eaeaea 0%,#f5f5f5 60%,#e6e6e6 100%)"></div>
  <div class="name">Product name</div><div class="price">$49.99</div>
</div>
<div class="abs product" style="left:379px;top:1086px">
  <div style="position:relative">
    <div class="ph" role="img" aria-label="Model in a black tie-shoulder peplum top" style="background:linear-gradient(180deg,#e8e6e4 0%,#cfcfcf 100%)"></div>
    <div class="shade"></div>
    <div class="add-bar">Add to cart</div>
  </div>
  <div class="name">Product name</div><div class="price">$49.99</div>
</div>
<div class="abs product" style="left:609px;top:1086px">
  <div class="ph" role="img" aria-label="Model in a multicolour striped shirt" style="background:linear-gradient(180deg,#f2f0ee 0%,#c65c3a 45%,#2c2c2c 85%,#f0eeec 100%)"></div>
  <div class="name">Product name</div><div class="price">$49.99</div>
</div>
<div class="abs product" style="left:841px;top:1086px">
  <div class="ph" role="img" aria-label="Model in a snake-print wrap blouse" style="background:linear-gradient(180deg,#ece8e3 0%,#c99c7c 50%,#e8e3de 100%)"></div>
  <div class="name">Product name</div><div class="price">$49.99</div>
</div>

<div class="abs sale-band"></div>
<div class="abs sale-frame"></div>
<div class="abs sale-photo-frame"></div>
<div class="abs sale-photo" role="img" aria-label="Laughing woman with long hair in a fringed dark crop top"></div>
<div class="abs sale-title">BIG SALE</div>
<div class="abs sale-sub">30% OFF DISCOUNT</div>
<p class="abs sale-text">Lorem Ipsum is simply dummy text of the printing and typesetting industry. Lorem Ipsum has been the industry's standard dummy text ever since the 1500s.</p>
<a class="abs btn-outline sale-btn" href="#">Shop now</a>

<h2 class="abs section-title" style="top:2126px">LATEST NEWS</h2>
<article class="abs news-card" style="left:149px">
  <div class="ph" role="img" aria-label="Red-haired woman in a red tee against a metal wall" style="background:linear-gradient(90deg,#5a5450 0%,#a8322f 45%,#6f7f86 100%)"></div>
  <div class="head">News headline</div><div class="date">22.06.2020</div>
  <p class="text">Lorem Ipsum is simply dummy text of the printing and typesetting industry. Lorem Ipsum has been the industry's standard dummy &nbsp;text ever since the 1500s.</p>
  <a class="more" href="#">READ MORE</a>
</article>
<article class="abs news-card" style="left:455px">
  <div class="ph" role="img" aria-label="Woman in a white graphic tee on a beach" style="background:linear-gradient(180deg,#a9d6e3 0%,#4fa7ad 40%,#d9e3e3 75%,#c9c2b5 100%)"></div>
  <div class="head">News headline</div><div class="date">22.06.2020</div>
  <p class="text">Lorem Ipsum is simply dummy text of the printing and typesetting industry. Lorem Ipsum has been the industry's standard dummy &nbsp;text ever since the 1500s.</p>
  <a class="more" href="#">READ MORE</a>
</article>
<article class="abs news-card" style="left:762px">
  <div class="ph" role="img" aria-label="Woman in a floral blouse and jeans beside a plant" style="background:linear-gradient(180deg,#cfcac3 0%,#b35a4a 45%,#6d8aa8 100%)"></div>
  <div class="head">News headline</div><div class="date">22.06.2020</div>
  <p class="text">Lorem Ipsum is simply dummy text of the printing and typesetting industry. Lorem Ipsum has been the industry's standard dummy &nbsp;text ever since the 1500s.</p>
  <a class="more" href="#">READ MORE</a>
</article>

<h2 class="abs section-title" style="top:2671px">TESTIMONIALS</h2>
<div class="abs arrow-box" style="left:52px;top:2734px"><svg width="10" height="16" viewBox="0 0 10 16" fill="none" stroke="#999" stroke-width="1.2"><path d="M8 1L2 8l6 7"/></svg></div>
<div class="abs arrow-box" style="left:1108px;top:2734px"><svg width="10" height="16" viewBox="0 0 10 16" fill="none" stroke="#999" stroke-width="1.2"><path d="M2 1l6 7-6 7"/></svg></div>
<p class="abs quote"><span class="qmark">&ldquo;</span> Lorem Ipsum is simply dummy text of the printing and typesetting industry. Lorem Ipsum has been the industry's standard dummy text ever<br>since the 1500s, when an unknown printer took a galley of type and scrambled it to make a type specimen book. <span class="qmark">&rdquo;</span></p>
<div class="abs t-name">LINA MARSH</div>
<div class="abs t-stars">&#9733;&#9733;&#9733;&#9733;&#9733;</div>
<div class="abs dots t-dots"><span class="on"></span><span></span><span></span><span></span></div>

<div class="abs service dark" style="left:147px;width:291px">
  <svg width="48" height="36" viewBox="0 0 48 36" fill="none" stroke="#fff" stroke-width="2"><path d="M12 6h20v20H12zM32 12h8l6 7v7h-14"/><circle cx="18" cy="29" r="4"/><circle cx="38" cy="29" r="4"/><path d="M2 12h8M4 18h6M6 24h4"/></svg>
  <div class="body"><h4>Free delivery</h4><p>Lorem Ipsum is simply dummy text of the printing and typesetting industry.</p></div>
</div>
<div class="abs service light" style="left:455px;width:289px">
  <svg width="44" height="46" viewBox="0 0 44 46" fill="none" stroke="#fff" stroke-width="2"><circle cx="22" cy="15" r="9"/><path d="M10 15a12 12 0 0124 0M10 13v6M34 13v6M4 45c0-10 8-16 18-16s18 6 18 16zM22 29l-5 8 5 8 5-8z"/></svg>
  <div class="body"><h4>Premium support</h4><p>Lorem Ipsum is simply dummy text of the printing and typesetting industry.</p></div>
</div>
<div class="abs service dark" style="left:761px;width:289px">
  <svg width="48" height="48" viewBox="0 0 48 48" fill="none" stroke="#fff" stroke-width="2"><path d="M8 18l16-8 16 8v18l-16 8-16-8zM8 18l16 8 16-8M24 26v18M14 6a14 14 0 0120 0l-2 5"/><path d="M30 3l4 3-3 4"/></svg>
  <div class="body"><h4>Return policy</h4><p>Lorem Ipsum is simply dummy text of the printing and typesetting industry.</p></div>
</div>

<footer class="abs site-footer"></footer>
<div class="abs footer-brand">Tavi Shirt Co.</div>
<ul class="abs contact-list">
  <li><svg width="12" height="12" viewBox="0 0 12 12" fill="#0b3f94"><path d="M2.5 1l2 2.5-1.2 1.3a7 7 0 003.9 3.9L8.5 7.5 11 9.5 9.8 11C5 11 1 7 1 2.2z"/></svg>+00 555 010 246</li>
  <li><svg width="12" height="12" viewBox="0 0 12 12" fill="#0b3f94"><rect x="3" y="1" width="6" height="3"/><rect x="1" y="4" width="10" height="5"/><rect x="3" y="8" width="6" height="3"/></svg>+00 555 010 247</li>
  <li><svg width="12" height="12" viewBox="0 0 12 12" fill="#0b3f94"><path d="M1 3h10v7H1zM1 3l5 4 5-4" stroke="#88ceeb" stroke-width=".8"/></svg>hello@tavishirt.example</li>
  <li><svg width="12" height="12" viewBox="0 0 12 12" fill="#0b3f94"><path d="M6 1a3.5 3.5 0 013.5 3.5C9.5 7 6 11 6 11S2.5 7 2.5 4.5A3.5 3.5 0 016 1z"/><circle cx="6" cy="4.5" r="1.2" fill="#88ceeb"/></svg>412 Maple Crest Lane</li>
  <li class="indent">Harlow, IL 60000</li>
</ul>
<div class="abs pay-row"><span></span><span></span><span></span><span></span><span></span></div>

<div class="abs footer-col" style="left:433px;top:3259px"><h5>Quick links</h5>
  <ul><li>Home</li><li>Collection</li><li>About</li><li>News</li><li>Sale</li><li>Contact</li></ul></div>
<div class="abs footer-col" style="left:601px;top:3259px"><h5>Accounts</h5>
  <ul><li>login</li><li>Signup</li><li>My Profile</li><li>My Cart</li><li>Checkout</li><li>Return Policy</li></ul></div>
<div class="abs footer-col" style="left:743px;top:3259px"><h5>Newsletter</h5></div>
<div class="abs news-input">Email Address</div>
<div class="abs news-btn">Subscribe</div>
<div class="abs social-row"><span class="fill"></span><span></span><span></span><span></span><span></span></div>

<div class="abs bottom-bar">
  <span class="copy">Copyright &copy; 2020 Tavi Shirt Co. All Rights Reserved.</span>
  <span class="legal">Privacy policy &nbsp;-&nbsp; Terms &amp; Conditions</span>
</div>

</body>
</html>
```